Book cover for New Book: Whispers Beneath Red Rock. Top of the cover-Corwin Ashby
Title:Whispers Beneath Red Rock
subtitle: Sometimes the past is best left buried
Author name: M. K. Brandvold
Picturing the background to be a piture of Monument Valley, Az. with stormy clouds-maybe a lightning bolt, and long shadows.
Need coverwith spine and blurb, front cover 2x2 pisture, Design must mee all Zephora and Listenry requirements. Cover 2500 H,1600W. 300DPI. Jpeg. 24 bit color, RGB.

```html
<!DOCTYPE html>
<html lang="en">
<head>
<meta charset="utf-8">
<title>Whispers Beneath Red Rock — Cover Wrap</title>
<link rel="stylesheet" href="https://fonts.googleapis.com/css2?family=Marcellus&family=Poppins:wght@400;500&display=swap">
<style>
  :root {
    --sky-dark: #0f0a07;
    --cloud-orange: #d9541a;
    --cloud-glow: #f58a2a;
    --rock-red: #7a2e15;
    --rock-deep: #2a120a;
    --sand: #c9732a;
    --ink-light: #ffffff;
    --title-light: #eeeeee;
  }
  * { margin: 0; padding: 0; box-sizing: border-box; }
  html, body { width: 1200px; height: 917px; overflow: hidden; background: var(--sky-dark); }
  .cover-wrap { position: relative; width: 1200px; height: 917px; overflow: hidden; }

  .backdrop-photo {
    position: absolute; inset: 0;
    background:
      radial-gradient(ellipse 360px 120px at 900px 330px, rgba(245,138,42,.85), transparent 70%),
      radial-gradient(ellipse 300px 90px at 1060px 230px, rgba(217,84,26,.7), transparent 70%),
      radial-gradient(ellipse 460px 110px at 420px 110px, rgba(217,84,26,.6), transparent 70%),
      radial-gradient(ellipse 300px 80px at 640px 200px, rgba(245,138,42,.55), transparent 70%),
      linear-gradient(180deg, var(--sky-dark) 0%, #24110a 18%, #3a190d 36%, var(--rock-deep) 48%, #4a1c0e 60%, var(--rock-red) 72%, #8a3b17 82%, var(--sand) 90%, #a9561f 100%);
  }

  .blurb {
    position: absolute; left: 53px; top: 218px; width: 466px;
    font-family: "Poppins", sans-serif; font-size: 16.8px; line-height: 25.3px;
    color: var(--ink-light); text-align: justify;
  }

  .code-box { position: absolute; left: 312px; top: 743px; width: 227px; height: 139px; background: #ffffff; }

  .spine-title, .spine-author {
    position: absolute; writing-mode: vertical-rl; transform: rotate(180deg);
    color: var(--ink-light); white-space: nowrap;
  }
  .spine-author {
    left: 584px; top: 72px; height: 204px;
    font-family: "Poppins", sans-serif; font-weight: 500; font-size: 24px; text-align: left;
  }
  .spine-title {
    left: 580px; top: 405px; height: 437px;
    font-family: "Marcellus", serif; font-size: 30px; letter-spacing: .5px; text-align: left;
  }

  .tagline {
    position: absolute; left: 700px; top: 24px; width: 426px; text-align: center;
    font-family: "Poppins", sans-serif; font-size: 21.5px; color: var(--ink-light);
  }

  .front-title {
    position: absolute; left: 680px; top: 0; width: 466px; height: 320px;
    font-family: "Marcellus", serif; color: var(--title-light); font-weight: 400;
  }
  .front-title span {
    position: absolute; left: 0; width: 100%; text-align: center; line-height: 1; white-space: nowrap;
  }
  .front-title .title-top { top: 80px; font-size: 84px; }
  .front-title .title-mid { top: 173px; font-size: 46px; }
  .front-title .title-bottom { top: 226px; font-size: 84px; }

  .front-author {
    position: absolute; left: 700px; top: 836px; width: 426px; text-align: center;
    font-family: "Poppins", sans-serif; font-weight: 500; font-size: 35px; color: var(--ink-light);
  }
</style>
</head>
<body>
<div class="cover-wrap">
  <div class="backdrop-photo" role="img" aria-label="Photograph placeholder: Monument Valley red rock spires under a stormy orange sky, with long shadows stretching across desert sand"></div>

  <p class="blurb">Lorem ipsum dolor sit amet, consectetuer adipiscing elit, sed diam nonummy nibh euismod tincidunt ut laoreet dolore magna aliquam Lorem ipsum dolor sit amet, consectetur adipiscing elit, sed do eiusmod tempor incididunt ut labore et dolore magna aliqua. Ut enim ad minim veniam, quis nostrud exercitation ullamco laboris nisi ut aliquip ex ea commodo consequat. Duis aute irure dolor in reprehenderit in voluptate velit esse cillum dolore eu fugiat nulla pariatur. Excepteur sint occaecat cupidatat non proident, sunt in culpa qui officia deserunt mollit anim id est laborum.</p>

  <div class="code-box"></div>

  <div class="spine-author">M. K. Brandvold</div>
  <div class="spine-title">WHISPERS BENEATH RED ROCK</div>

  <p class="tagline">Sometimes the past is best left buried</p>

  <h1 class="front-title">
    <span class="title-top">WHISPERS</span>
    <span class="title-mid">BENEATH</span>
    <span class="title-bottom">RED ROCK</span>
  </h1>

  <p class="front-author">M. K. Brandvold</p>
</div>
</body>
</html>
```